Flyer Design

I need a flyer as Iam starting a business which cleans Leather couches,sofas,chairs for residential and businesses.
We clean the interiors of automobiles and marine craft, boats large and small.
We would like to be able to get across the message that we are affordable, personal and reliable.
The Gold coast is our market and within this area there is a large amount of holiday apartments and houses which do experience high traffic to their living and dinning areas.

Target Market(s)

Target market Home,Apartment,Marine and Auto Owners

Industry/Entity Type

Residential

Requirements
Must have
• The flyer must have Company name which is BRIGHT HIDE CARE MOBILE NUMBER
0471932054
EMAIL marvtolk@quellnet.com
Colours would like bright Gold or green or Red eith black lettering very modern font
Nice to have
• I would like to keep it as simple and clean looking.but eye catching
Should not have
• Dont want the flyer to look like a Real Estate flyer or a pizza advertisement.

```html
<!DOCTYPE html>
<html lang="en">
<head>
<meta charset="utf-8">
<title>Bright Hide Care Mobile – Flyer</title>
<link rel="stylesheet" href="https://fonts.googleapis.com/css2?family=Bebas+Neue&family=Open+Sans:wght@300;400&display=swap">
<style>
  :root {
    --red: #d3202a;
    --red-deep: #b01c2b;
    --red-dark: #9e1a2a;
    --white: #ffffff;
    --band-grey: #e4e4e4;
    --page-bg: #ece8e3;
    --shadow: rgba(0, 0, 0, 0.35);
    --leather-light: #7a7a7a;
    --leather-mid: #4a4a4a;
    --leather-dark: #2c2c2c;
  }
  * { box-sizing: border-box; margin: 0; padding: 0; }
  html, body { width: 1200px; height: 900px; overflow: hidden; }
  body { background: var(--page-bg); position: relative; }

  .flyer {
    position: absolute;
    left: 303px; top: 57px;
    width: 594px; height: 778px;
    background: var(--white);
    overflow: hidden;
    box-shadow: 0 4px 14px rgba(0,0,0,0.25);
  }

  .flyer__header-bg {
    position: absolute; left: 0; top: 0; width: 100%; height: 145px;
    background: linear-gradient(180deg, var(--red) 0%, var(--red-deep) 100%);
  }
  .flyer__photo-band {
    position: absolute; left: 0; top: 143px; width: 100%; height: 92px;
    background: linear-gradient(180deg, var(--band-grey), #f6f6f6);
  }
  .flyer__base-bg { position: absolute; left: 0; top: 0; width: 594px; height: 778px; }

  .flyer__title {
    position: absolute; left: 0; top: 26px; width: 100%;
    text-align: center;
    font-family: "Bebas Neue", sans-serif;
    font-size: 57px; line-height: 1;
    letter-spacing: 1.5px;
    color: var(--white);
  }

  .service-photo {
    position: absolute; top: 106px; width: 181px; height: 124px;
    background: var(--white);
    padding: 9px 9px 10px;
    box-shadow: 0 10px 10px -4px var(--shadow);
  }
  .service-photo--boat { left: 15px; }
  .service-photo--lounge { left: 205px; }
  .service-photo--car { left: 395px; top: 103px; height: 127px; width: 183px; }
  .service-photo__fill { width: 100%; height: 100%; }
  .service-photo--boat .service-photo__fill {
    background:
      linear-gradient(180deg, rgba(150,165,180,0.55) 0%, rgba(255,255,255,0) 35%),
      linear-gradient(160deg, #c9d3dc 0%, #f1f3f5 45%, #d7dde2 70%, #a9b4bd 100%);
  }
  .service-photo--lounge .service-photo__fill {
    background:
      linear-gradient(180deg, rgba(0,0,0,0) 55%, rgba(236,228,214,0.9) 75%, #e9e1d2 100%),
      linear-gradient(100deg, #b7552a 0%, #cf7a3e 35%, #e2b07a 60%, #b45a2c 100%);
  }
  .service-photo--car .service-photo__fill {
    background:
      linear-gradient(180deg, rgba(120,160,210,0.8) 0%, rgba(60,70,80,0) 30%),
      linear-gradient(140deg, #5c6670 0%, #2f3236 50%, #3d4247 75%, #6a7076 100%);
  }

  .value-tag { position: absolute; top: 255px; width: 164px; height: 50px; }
  .value-tag--affordable { left: 29px; }
  .value-tag--personal { left: 214px; }
  .value-tag--reliable { left: 398px; }
  .value-tag svg { position: absolute; inset: 0; }
  .value-tag__label {
    position: absolute; left: 0; top: 0; width: 148px; height: 50px;
    display: flex; align-items: center; justify-content: center;
    font-family: "Bebas Neue", sans-serif; font-size: 23px;
    color: var(--white); letter-spacing: 0.3px;
  }

  .lounge-piece {
    position: absolute;
    background: linear-gradient(180deg, var(--leather-light) 0%, var(--leather-mid) 45%, var(--leather-dark) 80%, #444 100%);
    border-radius: 14px 14px 4px 4px;
    box-shadow: 0 6px 8px -4px rgba(0,0,0,0.4);
  }
  .lounge-piece--armchair-left { left: 12px; top: 356px; width: 180px; height: 148px; }
  .lounge-piece--sofa { left: 195px; top: 354px; width: 238px; height: 108px; }
  .lounge-piece--armchair-right { left: 436px; top: 358px; width: 146px; height: 130px; }

  .services {
    position: absolute; left: 0; top: 526px; width: 100%;
    text-align: center; color: var(--white);
    font-family: "Open Sans", sans-serif;
  }
  .services__heading { font-weight: 300; font-size: 25px; line-height: 1.2; }
  .services__text { font-weight: 400; font-size: 15px; line-height: 20px; margin-top: 2px; }

  .contact { position: absolute; top: 695px; height: 60px; }
  .contact--phone { left: 0; width: 282px; }
  .contact--email { left: 312px; width: 282px; }
  .contact svg.contact__bar { position: absolute; inset: 0; }
  .contact__content {
    position: absolute; top: 0; height: 60px;
    display: flex; align-items: center; gap: 16px;
    font-family: "Bebas Neue", sans-serif; color: var(--red);
  }
  .contact--phone .contact__content { left: 28px; font-size: 31px; }
  .contact--email .contact__content { left: 30px; font-size: 21px; gap: 9px; }

  .flyer__footer {
    position: absolute; left: 0; bottom: 0; width: 100%; height: 23px;
    background: var(--red-dark);
  }
</style>
</head>
<body>
  <main class="flyer">
    <svg class="flyer__base-bg" viewBox="0 0 594 778" aria-hidden="true">
      <defs>
        <linearGradient id="baseRed" x1="0" y1="0" x2="0" y2="1">
          <stop offset="0" stop-color="#d52129"/>
          <stop offset="0.7" stop-color="#c61f2a"/>
          <stop offset="1" stop-color="#a81b2b"/>
        </linearGradient>
      </defs>
      <path d="M0 478 Q300 438 594 462 L594 778 L0 778 Z" fill="url(#baseRed)"/>
    </svg>

    <div class="flyer__header-bg"></div>
    <div class="flyer__photo-band"></div>

    <h1 class="flyer__title">BRIGHT HIDE CARE MOBILE</h1>

    <figure class="service-photo service-photo--boat">
      <div class="service-photo__fill" role="img" aria-label="White leather seats on the deck of a boat"></div>
    </figure>
    <figure class="service-photo service-photo--lounge">
      <div class="service-photo__fill" role="img" aria-label="Cream leather lounge chairs in a timber-panelled cabin"></div>
    </figure>
    <figure class="service-photo service-photo--car">
      <div class="service-photo__fill" role="img" aria-label="Black leather rear seats inside a car"></div>
    </figure>

    <div class="value-tag value-tag--affordable">
      <svg viewBox="0 0 164 50" aria-hidden="true"><polygon points="0,0 148,0 164,25 148,50 0,50" fill="var(--red)"/></svg>
      <span class="value-tag__label">AFFORDABLE</span>
    </div>
    <div class="value-tag value-tag--personal">
      <svg viewBox="0 0 164 50" aria-hidden="true"><polygon points="0,0 148,0 164,25 148,50 0,50" fill="var(--red)"/></svg>
      <span class="value-tag__label">PERSONAL</span>
    </div>
    <div class="value-tag value-tag--reliable">
      <svg viewBox="0 0 164 50" aria-hidden="true"><polygon points="0,0 148,0 164,25 148,50 0,50" fill="var(--red)"/></svg>
      <span class="value-tag__label">RELIABLE</span>
    </div>

    <div class="lounge-piece lounge-piece--armchair-left" role="img" aria-label="Black leather armchair"></div>
    <div class="lounge-piece lounge-piece--sofa" role="img" aria-label="Black leather three-seater sofa"></div>
    <div class="lounge-piece lounge-piece--armchair-right" role="img" aria-label="Black leather armchair"></div>

    <section class="services">
      <h2 class="services__heading">We clean</h2>
      <p class="services__text">leather couches, sofas, chairs for residential and<br>businesses, the interiors of automobiles and<br>marine craft, boats large and small.</p>
    </section>

    <div class="contact contact--phone">
      <svg class="contact__bar" viewBox="0 0 282 60" aria-hidden="true"><polygon points="0,0 252,0 282,30 252,60 0,60" fill="var(--white)"/></svg>
      <div class="contact__content">
        <svg width="20" height="32" viewBox="0 0 20 32" aria-hidden="true">
          <rect x="2" y="4" width="16" height="27" rx="3" fill="var(--red)"/>
          <rect x="4" y="0" width="3" height="6" fill="var(--red)"/>
          <rect x="5" y="8" width="10" height="8" fill="var(--white)"/>
          <circle cx="10" cy="24" r="2.5" fill="var(--white)"/>
        </svg>
        <span class="contact__value">0471932054</span>
      </div>
    </div>

    <div class="contact contact--email">
      <svg class="contact__bar" viewBox="0 0 282 60" aria-hidden="true"><polygon points="30,0 282,0 282,60 30,60 0,30" fill="var(--white)"/></svg>
      <div class="contact__content">
        <svg width="36" height="24" viewBox="0 0 38 26" aria-hidden="true">
          <rect x="1.5" y="1.5" width="35" height="23" fill="none" stroke="var(--red)" stroke-width="3"/>
          <polyline points="2,2 19,15 36,2" fill="none" stroke="var(--red)" stroke-width="3"/>
          <line x1="2" y1="24" x2="14" y2="12" stroke="var(--red)" stroke-width="2.5"/>
          <line x1="36" y1="24" x2="24" y2="12" stroke="var(--red)" stroke-width="2.5"/>
        </svg>
        <span class="contact__value">MARVTOLK@QUELLNET.COM</span>
      </div>
    </div>

    <div class="flyer__footer"></div>
  </main>
</body>
</html>
```